hi all

Im after a new age looking business card with my company logo on it

must include these details, I would like the PH and Email to be symbols

If the colours used for card could be kept within the colours used in logo that I have supplied that would be great, if another colour is to be used dark grey would be ok. no light bulbs etc thanks

Details below to be incorporated on card

Damian Holloway

Lic E871302

PH 0219647381

E info@brightvaleelectrical.example.nz

Domestic Commercial Industrial Electricians

```html
<!DOCTYPE html>
<html lang="en">
<head>
<meta charset="utf-8">
<title>Brightvale Electrical – Business Card</title>
<link rel="stylesheet" href="https://fonts.googleapis.com/css2?family=Catamaran:wght@500;600;700&display=swap">
<style>
  :root {
    --blue-deep: #0a5a9c;
    --blue-slate: #3a5679;
    --brand-blue: #0f74bd;
    --panel-light: #e6e7e9;
    --panel-glow: #ffffff;
    --charcoal: #1e1f21;
    --ink-dark: #1b1b1b;
    --white: #ffffff;
  }
  * { margin: 0; padding: 0; box-sizing: border-box; }
  html, body {
    width: 1200px;
    height: 686px;
    overflow: hidden;
    background: var(--white);
  }
  .card {
    position: relative;
    width: 1200px;
    height: 686px;
    overflow: hidden;
    font-family: "Catamaran", "Segoe UI", sans-serif;
    color: var(--white);
  }
  .card-backdrop {
    position: absolute;
    inset: 0;
    width: 1200px;
    height: 686px;
  }
  .details {
    position: absolute;
    left: 76px;
    top: 0;
    width: 521px;
    height: 686px;
  }
  .name {
    position: absolute;
    left: 0;
    top: 114px;
    font-size: 49px;
    font-weight: 600;
    line-height: 58px;
    white-space: nowrap;
    letter-spacing: -0.3px;
  }
  .name-surname {
    display: inline-block;
    background: var(--white);
    color: var(--brand-blue);
    border-radius: 14px;
    padding: 0 8px;
    margin-left: 4px;
  }
  .contact {
    position: absolute;
    left: 0;
    display: flex;
    align-items: center;
    gap: 18px;
    font-weight: 600;
    white-space: nowrap;
  }
  .contact-phone { top: 212px; font-size: 31px; }
  .contact-email { top: 294px; font-size: 24px; }
  .contact-icon { flex: none; fill: var(--white); }
  .rule {
    position: absolute;
    left: 0;
    width: 521px;
    height: 2px;
    background: var(--white);
  }
  .rule-top { top: 377px; }
  .rule-bottom { top: 518px; }
  .services {
    position: absolute;
    left: 6px;
    top: 406px;
    line-height: 1;
  }
  .services-lead { display: block; font-size: 30px; font-weight: 600; }
  .services-main { display: block; font-size: 40px; font-weight: 600; margin-top: 6px; }
  .licence {
    position: absolute;
    left: 6px;
    top: 538px;
    font-size: 27px;
    font-weight: 600;
  }
  .brand {
    position: absolute;
    left: 620px;
    top: 200px;
    width: 520px;
    display: flex;
    flex-direction: column;
    align-items: center;
    gap: 22px;
  }
  .brand-mark {
    width: 74px;
    height: 74px;
    border-radius: 50%;
    background: var(--brand-blue);
  }
  .brand-name {
    color: var(--brand-blue);
    font-size: 38px;
    font-weight: 700;
    letter-spacing: 4px;
    text-transform: uppercase;
    white-space: nowrap;
  }
</style>
</head>
<body>
  <main class="card">
    <svg class="card-backdrop" viewBox="0 0 1200 686" aria-hidden="true">
      <defs>
        <linearGradient id="blue-field" x1="0" y1="0" x2="1" y2="0.3">
          <stop offset="0" stop-color="var(--blue-deep)"/>
          <stop offset="1" stop-color="var(--blue-slate)"/>
        </linearGradient>
        <radialGradient id="light-field" cx="870" cy="350" r="320" gradientUnits="userSpaceOnUse">
          <stop offset="0" stop-color="var(--panel-glow)"/>
          <stop offset="1" stop-color="var(--panel-light)"/>
        </radialGradient>
      </defs>
      <rect class="backdrop-blue" width="1200" height="686" fill="url(#blue-field)" role="img" aria-label="Soft blue background with faint geometric texture"/>
      <path class="backdrop-light" d="M620 0 L1200 0 L1200 686 L620 686 L597 642 L597 44 Z" fill="url(#light-field)"/>
      <path class="backdrop-edge" d="M1185 0 L1200 0 L1200 686 L1185 686 Q1158 640 1158 560 L1158 130 Q1158 45 1185 0 Z" fill="var(--charcoal)"/>
    </svg>

    <section class="details">
      <h1 class="name">Damian <span class="name-surname">Holloway</span></h1>

      <p class="contact contact-phone">
        <svg class="contact-icon" width="30" height="32" viewBox="0 0 30 32" aria-label="Phone">
          <path d="M9 2 h14 a3 3 0 0 1 3 3 v22 a3 3 0 0 1 -3 3 h-14 a3 3 0 0 1 -3 -3 v-22 a3 3 0 0 1 3 -3 Z M11 6 v18 h10 v-18 Z M14 26 h4 v2 h-4 Z"/>
          <path d="M1 12 q0 -5 4 -6 v20 q-4 -1 -4 -6 Z"/>
        </svg>
        <span>0219647381</span>
      </p>

      <p class="contact contact-email">
        <svg class="contact-icon" width="30" height="22" viewBox="0 0 30 22" aria-label="Email">
          <path d="M1 1 h28 v20 h-28 Z M3 3 v1 l12 9 l12 -9 v-1 Z M3 7 v12 h24 v-12 l-12 9 Z"/>
        </svg>
        <span>info@brightvaleelectrical.example.nz</span>
      </p>

      <div class="rule rule-top"></div>
      <p class="services">
        <span class="services-lead">Domestic Commercial</span>
        <span class="services-main">Industrial Electricians</span>
      </p>
      <div class="rule rule-bottom"></div>

      <p class="licence">Lic E871302</p>
    </section>

    <section class="brand">
      <div class="brand-mark"></div>
      <p class="brand-name">Brightvale Electrical</p>
    </section>
  </main>
</body>
</html>
```